Property casualty insurance consultant. Review business insurance plans and provide risk mgmt advice

Front side: logo, tag line, name and info
Back side: Services

Front:
Marcus T. Dole
Property / Casualty Insurance Consulting and Training
P.O. Box 7386
Greensboro, NC 27519
marcus@brightfenpartners.example 336-555-0147 www.brightfenpartners.example
Back side:
Insurance Program Review
Renewal Proposal Review
Safety Planning / Loss Control
Disaster Planning
Claims Assistance
Updates

Images uploaded. I am non tech so let me know if this did not work. Choose image with Blue Fonts and Orange design element. The brief has also changed to put all info on front and services on back. Thank you.

Reason: took a while to get images downloaded

Going through elimination process. Thanks to all. On any revisions, please add two more services on reverse: Company Training . Agency Training

Target Market(s)

Business owners of all sizes and types

Industry/Entity Type

Insurance

Requirements
Must have
• Logo will have the colors to use, info fonts probably black and should closely match that in logo. Front side, logo, tag line, name and info. Back side with services and logo design element incorporated somehow

```html
<!DOCTYPE html>
<html lang="en">
<head>
<meta charset="utf-8">
<title>Brightfen Partners – Business Cards</title>
<link href="https://fonts.googleapis.com/css2?family=Lato:wght@400;700;900&display=swap" rel="stylesheet">
<style>
  :root {
    --stage: #2b2b2d;
    --navy: #0f2a6b;
    --navy-card: #0b3a8c;
    --orange: #e8731e;
    --gold: #f4a21c;
    --ink: #111111;
    --paper: #ffffff;
  }
  * { margin: 0; padding: 0; box-sizing: border-box; }
  html, body { width: 1200px; height: 900px; overflow: hidden; }
  body {
    background: var(--stage);
    font-family: "Lato", sans-serif;
    position: relative;
  }
  .card {
    position: absolute;
    width: 640px;
    height: 366px;
    border-radius: 4px;
    box-shadow: 0 12px 30px rgba(0,0,0,.45);
    overflow: hidden;
  }

  /* Back side: services */
  .card-back {
    left: 80px; top: 50px;
    background: linear-gradient(135deg, #0d4399 0%, var(--navy-card) 60%, #08306f 100%);
    color: var(--paper);
  }
  .card-back .brand {
    position: absolute; left: 60px; top: 48px;
    display: flex; align-items: center; gap: 14px;
  }
  .brand-dot {
    width: 22px; height: 22px; border-radius: 50%;
    background: var(--gold);
    flex: none;
  }
  .brand-name {
    font-weight: 700;
    font-size: 34px;
    letter-spacing: 1px;
    text-transform: uppercase;
    white-space: nowrap;
  }
  .card-back .brand-name { color: var(--paper); }
  .services {
    position: absolute; left: 150px; top: 118px;
    list-style: none;
    font-weight: 700; font-size: 23px; line-height: 36px;
    color: #e8eef8;
  }

  /* Front side: contact */
  .card-front {
    left: 480px; top: 474px;
    background: var(--paper);
  }
  .card-front .brand {
    position: absolute; left: 34px; top: 100px;
    display: flex; align-items: center; gap: 12px;
  }
  .card-front .brand-dot { width: 20px; height: 20px; }
  .card-front .brand-name { color: var(--navy); font-size: 24px; letter-spacing: .5px; }
  .swoosh { position: absolute; left: 30px; top: 122px; }
  .title-block {
    position: absolute; right: 34px; top: 26px;
    text-align: right; text-transform: uppercase;
    white-space: nowrap;
  }
  .person-name { color: var(--orange); font-weight: 900; font-size: 20px; letter-spacing: .5px; line-height: 24px; }
  .role { color: var(--navy); font-weight: 700; font-size: 14px; line-height: 20px; margin-top: 4px; }
  .address {
    position: absolute; right: 34px; top: 178px;
    text-align: right; color: var(--navy);
    font-weight: 900; font-size: 18px; line-height: 24px;
  }
  .contact {
    position: absolute; left: 34px; bottom: 30px;
    list-style: none; color: var(--ink);
    font-weight: 700; font-size: 18px; line-height: 30px;
  }
  .contact li { display: flex; align-items: center; gap: 10px; white-space: nowrap; }
  .contact .web { color: var(--navy); font-weight: 900; font-size: 20px; }
  .icon { width: 18px; height: 18px; fill: var(--ink); flex: none; }
</style>
</head>
<body>

<section class="card card-back" aria-label="Card back: services">
  <div class="brand">
    <span class="brand-dot"></span>
    <span class="brand-name">Brightfen Partners</span>
  </div>
  <ul class="services">
    <li>Loss Control</li>
    <li>Safety Planning</li>
    <li>Disaster Planning</li>
    <li>Claims Assistance</li>
    <li>Insurance Program Review</li>
    <li>Renewal Proposal Review</li>
  </ul>
</section>

<section class="card card-front" aria-label="Card front: contact details">
  <div class="title-block">
    <div class="person-name">Marcus T. Dole</div>
    <div class="role">Property / Casualty<br>Insurance Consulting &amp; Training</div>
  </div>
  <div class="brand">
    <span class="brand-dot"></span>
    <span class="brand-name">Brightfen Partners</span>
  </div>
  <svg class="swoosh" width="580" height="30" viewBox="0 0 580 30" aria-hidden="true">
    <defs>
      <linearGradient id="rule-fade" x1="0" x2="1">
        <stop offset="0" stop-color="#e8731e" stop-opacity="0"/>
        <stop offset=".5" stop-color="#e8731e"/>
        <stop offset="1" stop-color="#e8731e"/>
      </linearGradient>
    </defs>
    <path d="M0 26 Q 300 18 580 4" stroke="url(#rule-fade)" stroke-width="2" fill="none"/>
  </svg>
  <div class="address">
    P.O. Box 7386<br>Greensboro, NC 27519
  </div>
  <ul class="contact">
    <li>
      <svg class="icon" viewBox="0 0 24 24" aria-hidden="true"><path d="M4 9c0-3 4-5 8-5s8 2 8 5v2h-4V9c-1-1-3-1-4-1s-3 0-4 1v2H4zM6 12h12l2 8H4z"/></svg>
      336-555-0147
    </li>
    <li>
      <svg class="icon" viewBox="0 0 24 24" aria-hidden="true"><path d="M2 5h20v14H2zM4 7v1l8 5 8-5V7l-8 5z"/></svg>
      marcus@brightfenpartners.example
    </li>
    <li class="web">www.brightfenpartners.example</li>
  </ul>
</section>

</body>
</html>
```